Private Medical Clinic needs a letterhead design

Letterhead that can be edited. Letter head is needed for printing official doctor's notes, referrals, etc in a medical clinic. The letterhead should use the attached logos

```html
<!DOCTYPE html>
<html lang="en">
<head>
<meta charset="utf-8">
<title>Tall Pines Family Medicine – Letterhead</title>
<link rel="stylesheet" href="https://fonts.googleapis.com/css2?family=Roboto:wght@400;700&display=swap">
<style>
  :root {
    --ink: #2f362d;
    --brand: #454c42;
    --paper: #ffffff;
    --band: #434b3f;
  }
  html, body {
    margin: 0;
    padding: 0;
    overflow: hidden;
    background: var(--paper);
  }
  .letterhead {
    position: relative;
    width: 932px;
    height: 1200px;
    background: var(--paper);
    font-family: "Roboto", Arial, sans-serif;
    color: var(--ink);
    overflow: hidden;
  }
  .brand-name {
    position: absolute;
    left: 84px;
    top: 92px;
    margin: 0;
    font-family: "Roboto", Arial, sans-serif;
    font-weight: 400;
    color: var(--brand);
    line-height: 1;
  }
  .brand-name .brand-main {
    display: block;
    font-size: 44px;
    letter-spacing: -0.5px;
  }
  .brand-name .brand-sub {
    display: block;
    margin-top: 12px;
    margin-left: 2px;
    font-size: 12px;
    letter-spacing: 1.6px;
  }
  .contact {
    position: absolute;
    left: 644px;
    top: 70px;
    height: 110px;
    padding-left: 24px;
    border-left: 1.5px solid var(--ink);
    font-size: 13.2px;
    line-height: 16.5px;
  }
  .contact-name {
    margin: 0;
    font-weight: 700;
    font-size: 13.2px;
  }
  .contact-address {
    margin: 0;
    font-style: normal;
  }
  .contact-list {
    list-style: none;
    margin: 8px 0 0;
    padding: 0;
  }
  .contact-list li {
    display: flex;
    align-items: center;
    height: 18.5px;
  }
  .contact-list svg {
    width: 11px;
    height: 11px;
    margin-right: 9px;
    fill: var(--ink);
    flex: none;
  }
  .footer-band {
    position: absolute;
    left: 0;
    bottom: 0;
    width: 100%;
    height: 18px;
    background: var(--band);
  }
</style>
</head>
<body>
  <main class="letterhead">
    <h1 class="brand-name">
      <span class="brand-main">Tall Pines</span>
      <span class="brand-sub">FAMILY MEDICINE</span>
    </h1>

    <section class="contact">
      <p class="contact-name">Tall Pines Family Medicine</p>
      <address class="contact-address">4120 Larkspur Road<br>Fairbanks, Alaska 99701</address>
      <ul class="contact-list">
        <li>
          <svg viewBox="0 0 24 24" aria-hidden="true"><path d="M6.6 10.8a15.2 15.2 0 0 0 6.6 6.6l2.2-2.2a1 1 0 0 1 1-.25 11.4 11.4 0 0 0 3.6.57 1 1 0 0 1 1 1V20a1 1 0 0 1-1 1A17 17 0 0 1 3 4a1 1 0 0 1 1-1h3.5a1 1 0 0 1 1 1c0 1.25.2 2.45.57 3.57a1 1 0 0 1-.25 1z"/></svg>
          555-214-7730
        </li>
        <li>
          <svg viewBox="0 0 24 24" aria-hidden="true"><path d="M2 5h20v14H2z M3.5 6.5 12 13l8.5-6.5" fill="none" stroke="#2f362d" stroke-width="0"/><path d="M2 5h20v2l-10 7L2 7z"/><path d="M2 9l10 7 10-7v10H2z"/></svg>
          hello@tallpinesfm.com
        </li>
        <li>
          <svg viewBox="0 0 24 24" aria-hidden="true"><circle cx="12" cy="12" r="10"/><path d="M8 6c2 1 1 3 3 3s1 3-1 3-2 3 0 5M15 5c-1 2 1 3 3 3M16 14c1 0 2 1 1 3" fill="none" stroke="#ffffff" stroke-width="1.6"/></svg>
          www.tallpinesfm.com
        </li>
      </ul>
    </section>

    <div class="footer-band"></div>
  </main>
</body>
</html>
```